Halvex Consulting

Hi,
I have my own network consulting business (just me)
and need to get a logo and business card design together,

Based in New Zealand,

Gareth Pollard
Unified Communications and Network Architect

/design engineer,
and would like this to be the basis for personal branding and company identity

Reason: I will be off site for a couple of days - so you have some more time

Business

• I have the basis for a optional logo - needs color -

```html
<!DOCTYPE html>
<html lang="en">
<head>
<meta charset="utf-8">
<title>Halvex Consulting – Business Card</title>
<link href="https://fonts.googleapis.com/css2?family=Exo+2:ital,wght@0,300;1,400;1,500;1,600;1,700&display=swap" rel="stylesheet">
<style>
  :root {
    --page: #ffffff;
    --card-light: #f6f6f6;
    --card-edge: #e3e3e3;
    --ink-dark: #0b0b0b;
    --ink-mid: #2f2f2f;
    --ink-soft: #6b6b6b;
    --band: #3c3c3c;
    --accent: #2fd6f2;
    --accent-deep: #1e9fe0;
    --white: #ffffff;
  }
  html, body {
    margin: 0;
    width: 1200px;
    height: 960px;
    overflow: hidden;
    background: var(--page);
  }
  .canvas { display: block; width: 1200px; height: 960px; }
  .brand-name {
    font-family: "Exo 2", sans-serif;
    font-weight: 300;
    font-size: 19px;
    fill: var(--accent-deep);
  }
  .person-name {
    font-family: "Exo 2", sans-serif;
    font-style: italic;
    font-weight: 600;
    font-size: 27px;
    fill: var(--white);
  }
  .person-role {
    font-family: "Exo 2", sans-serif;
    font-style: italic;
    font-weight: 500;
    font-size: 13px;
    fill: var(--white);
  }
  .contact-line {
    font-family: "Exo 2", sans-serif;
    font-style: italic;
    font-weight: 500;
    font-size: 11px;
    letter-spacing: 4px;
    fill: var(--white);
  }
  .web-address {
    font-family: "Exo 2", sans-serif;
    font-style: italic;
    font-weight: 700;
    font-size: 21px;
    fill: var(--white);
  }
  .icon-ring { fill: none; stroke: var(--white); stroke-width: 1.2; }
  .icon-glyph { fill: none; stroke: var(--white); stroke-width: 1; stroke-linejoin: round; stroke-linecap: round; }
</style>
</head>
<body>
<svg class="canvas" viewBox="0 0 1200 960" xmlns="http://www.w3.org/2000/svg">
  <defs>
    <radialGradient id="card-surface" cx="0.45" cy="0.4" r="0.75">
      <stop offset="0" stop-color="var(--card-light)"/>
      <stop offset="1" stop-color="var(--card-edge)"/>
    </radialGradient>
    <linearGradient id="front-sweep" x1="0" y1="1" x2="1" y2="0.35">
      <stop offset="0" stop-color="var(--ink-soft)"/>
      <stop offset="0.45" stop-color="var(--ink-mid)"/>
      <stop offset="1" stop-color="var(--ink-dark)"/>
    </linearGradient>
    <linearGradient id="back-sweep" x1="1" y1="1" x2="0" y2="0.6">
      <stop offset="0" stop-color="var(--ink-soft)"/>
      <stop offset="0.5" stop-color="var(--ink-mid)"/>
      <stop offset="1" stop-color="var(--ink-dark)"/>
    </linearGradient>
    <linearGradient id="accent-fill" x1="0" y1="0" x2="0" y2="1">
      <stop offset="0" stop-color="#8ff1ff"/>
      <stop offset="1" stop-color="var(--accent)"/>
    </linearGradient>
    <clipPath id="card-shape">
      <rect width="695" height="395" rx="32"/>
    </clipPath>
  </defs>

  <!-- Front of card -->
  <g class="card-front" transform="translate(257 66)">
    <g clip-path="url(#card-shape)">
      <rect width="695" height="395" fill="url(#card-surface)"/>
      <path d="M71 395 C 200 185, 410 68, 695 59 L695 395 Z" fill="url(#front-sweep)"/>
      <rect class="contact-band" x="352" y="326" width="343" height="11" fill="var(--band)"/>
    </g>
    <circle class="brand-dot" cx="96" cy="75" r="20" fill="url(#accent-fill)"/>
    <text class="brand-name" x="15" y="131">Halvex Consulting</text>

    <text class="person-name" x="420" y="264" text-anchor="middle">Gareth Pollard</text>
    <rect class="name-rule" x="288" y="266" width="262" height="3" rx="1.5" fill="var(--accent)"/>
    <text class="person-role" x="420" y="291" text-anchor="middle">Unified Communications and Network Architect</text>

    <g class="contact-phone">
      <circle class="icon-ring" cx="418" cy="356" r="8"/>
      <path class="icon-glyph" d="M414.5 351.5 l2 -0.5 l1.3 2.7 l-1.3 1 q1 2.4 3.3 3.4 l1 -1.3 l2.7 1.3 l-0.5 2 q-6.5 0.4 -8.5 -8.6z"/>
      <text class="contact-line" x="439" y="360">0 482 736 519</text>
    </g>
    <g class="contact-email">
      <circle class="icon-ring" cx="418" cy="377" r="8"/>
      <rect class="icon-glyph" x="413.5" y="373.5" width="9" height="7"/>
      <path class="icon-glyph" d="M413.5 373.5 l4.5 4 l4.5 -4"/>
      <text class="contact-line" x="439" y="381">gareth@halvex.net</text>
    </g>
  </g>

  <!-- Back of card -->
  <g class="card-back" transform="translate(257 500)">
    <g clip-path="url(#card-shape)">
      <rect width="695" height="395" fill="url(#card-surface)"/>
      <path d="M0 58 C 250 62, 515 170, 623 395 L0 395 Z" fill="url(#back-sweep)"/>
    </g>
    <circle class="brand-dot" cx="606" cy="84" r="42" fill="url(#accent-fill)"/>
    <text class="web-address" x="41" y="378">www.halvexconsulting.com</text>
  </g>
</svg>
</body>
</html>
```